Updated brief for New ecommerce site needs a stunning business card that links to web site.

Updated business card brief. Please refer to the new files uploaded today (the last two) which show the background colour/style that we will be using in our web template for on-line trading, the grey marble concrete look.

Please see if you can use the grey marble background in the business card design in a way so it relates to our web template. It also needs to be transferable to banner ad, chatterbox ad etc.
vantor hub is a NEW eCommerce website which is commencing selling via bidnook & swapcrate, used & damaged mobile phones & accessories, evolving into a full eCommerce store.

We like strong clean lines, use of a circle, in essence this will become our logo as well. Colours strong orange/Black/White The orange stronger than in PixelHerd #8164937 & grey marble as per file attached #274615

We love the use of a circle!! As we are evolving & moving forward this is what the circle represents to us……. ongoing change.

Front side with a circle with vantor hub in a modern font in the middle, vantor is in a strong orange and group is in black or white. On the reverse side, use layout as per Snapwell design from plonk.com. for icon details (not the boarder at top/botto).

This design is to meet www.plonk.com luxe cards specifications
Thank you we look forward to last minute inspiration.

Project Deadline Extended Reason: Hi We need to extend our deadline to ensure we don't rush the design. We are close to getting what we want, however due to work commitments here we need a couple more days to work this through to ensure the concept ties in with our other marketing.Thank you for understanding and your patience.vantorhub Added Tuesday, March 3, 2015

Target Market(s)

Suppliers & business networking

Industry/Entity Type

Business

Contact Information for Business Card

Liam Presk
Director
mob +61 4987 6543
Locked Bag WXYZ 5678 QRS
liam@vantorhub.example.au
www.vantorhub.example.au

Requirements
Must have
• Design to meet www.plonk.com luxe business card specifications
• Colours - orange needs to be bold and strong & /black/white
• Circle with vantor hub in the middle
Nice to have
• Grey marble background incorporated into design in someway so it links with our web page.

```html
<!DOCTYPE html>
<html lang="en">
<head>
<meta charset="utf-8">
<title>vantor hub business cards</title>
<link rel="stylesheet" href="https://fonts.googleapis.com/css2?family=Open+Sans:wght@400;600;800&display=swap">
<style>
  :root {
    --page: #d9d6d2;
    --orange: #e8561f;
    --orange-deep: #c9441a;
    --black: #0b0b0b;
    --white: #ffffff;
    --marble-light: #f1f1f1;
    --marble-mid: #d3d3d3;
    --ink: #2a2a2a;
  }
  * { box-sizing: border-box; margin: 0; padding: 0; }
  html, body {
    width: 1200px; height: 1023px; overflow: hidden;
    background: var(--page);
    font-family: "Open Sans", Arial, sans-serif;
  }
  .sheet {
    position: relative; width: 1200px; height: 1023px;
    display: flex; align-items: center; justify-content: center; gap: 48px;
  }
  .card {
    position: relative; width: 540px; height: 310px; overflow: hidden;
    box-shadow: 0 8px 22px rgba(0,0,0,.25);
  }
  .marble {
    position: absolute; inset: 0;
    background: radial-gradient(ellipse at 30% 30%, var(--marble-light), var(--marble-mid));
  }
  .card--front .emblem {
    position: absolute; left: 36px; top: 50%; transform: translateY(-50%);
    width: 220px; height: 220px; border-radius: 50%;
    background: var(--black); border: 4px solid var(--white);
    box-shadow: 0 0 0 1px #bbb;
    display: flex; align-items: center; justify-content: center;
  }
  .wordmark {
    font-weight: 800; font-size: 34px; letter-spacing: 3px;
    text-transform: uppercase; text-align: center; line-height: 1.1;
  }
  .card--front .wordmark { color: var(--white); }
  .contact {
    position: absolute; left: 290px; top: 70px;
    color: var(--ink); font-size: 14px;
  }
  .contact__name {
    font-size: 19px; font-weight: 600; color: var(--orange);
    margin-bottom: 14px;
  }
  .contact__role {
    color: var(--ink); font-weight: 400; font-size: 15px;
    border-left: 1px solid var(--ink); padding-left: 6px; margin-left: 4px;
  }
  .contact__line { display: flex; align-items: center; gap: 8px; margin-bottom: 9px; }
  .contact__icon { width: 12px; height: 12px; flex: none; }
  .contact__address { margin-top: 6px; }
  .card--back {
    background: radial-gradient(ellipse at 50% 45%, #f06a2a, var(--orange-deep));
  }
  .card--back .emblem {
    position: absolute; left: 50%; top: 50%; transform: translate(-50%, -50%);
    width: 200px; height: 200px; border-radius: 50%; overflow: hidden;
    border: 6px solid var(--black);
    display: flex; align-items: center; justify-content: center;
  }
  .card--back .wordmark { position: relative; color: var(--black); font-size: 30px; }
</style>
</head>
<body>
<main class="sheet">
  <section class="card card--front">
    <div class="marble" role="img" aria-label="Grey marble texture background"></div>
    <div class="emblem">
      <span class="wordmark">vantor<br>hub</span>
    </div>
    <div class="contact">
      <p class="contact__name">Liam Presk<span class="contact__role">Director</span></p>
      <p class="contact__line">
        <svg class="contact__icon" viewBox="0 0 12 12"><rect width="12" height="12" rx="2" fill="var(--orange)"/><path d="M3.5 3l1.5 0 .6 1.6-.9.7a4 4 0 0 0 2 2l.7-.9 1.6.6v1.5A5.5 5.5 0 0 1 3.5 3z" fill="#fff"/></svg>
        +61 4987 6543
      </p>
      <p class="contact__line">
        <svg class="contact__icon" viewBox="0 0 12 12"><rect width="12" height="12" rx="2" fill="var(--orange)"/><rect x="2.5" y="3.5" width="7" height="5" fill="none" stroke="#fff"/><path d="M2.5 3.5l3.5 3 3.5-3" fill="none" stroke="#fff"/></svg>
        liam@vantorhub.example.au
      </p>
      <p class="contact__line">
        <svg class="contact__icon" viewBox="0 0 12 12"><rect width="12" height="12" rx="2" fill="var(--orange)"/><circle cx="6" cy="6" r="3.3" fill="none" stroke="#fff"/><path d="M2.7 6h6.6M6 2.7v6.6" stroke="#fff" stroke-width=".8"/></svg>
        www.vantorhub.example.au
      </p>
      <p class="contact__line contact__address">Locked Bag WXYZ 5678 QRS</p>
    </div>
  </section>

  <section class="card card--back">
    <div class="emblem">
      <div class="marble" role="img" aria-label="Grey marble texture inside the circle"></div>
      <span class="wordmark">vantor<br>hub</span>
    </div>
  </section>
</main>
</body>
</html>
```